Poster Design with Yoga Foam Roller Exercise Guide

Hi there!
We are looking for a poster design for our yoga foam roller product.
1. Foam roller.jpg shows our product. The poster is going to be wrapped around the roller
2. Poster dimensions: 42x28.5cm.
3. Design style matches our reference box.png and reference flat.png (colors, typefaces, overall look & feel)
4. Also check reference poster.jpg as a reference design for use of colors and overall look & feel
5. Written instructions are to be taken from written instructions.pdf
6. Illustrations are to be taken from illustrations.zip
7. Also use illustrations #2, 3 and 8 from girls.jpg, but add faces and change girl's hair (according to hair.jpg)
8. please see "orchard pals. jpg" for the ambience of the colours (instead of green, please use a brown colour). the base colours must be plain, without grain.
9. Please also create a small label design (53x17mm, to be inserted into a socket in the foam roller, see label.jpg). Please use our logo (reference box/reference flat/logo.jpg) and/or „Velvet Harbor“ as text as you see fit.
Thank you very much, we are really excited about receiving your designs :)

```html
<!DOCTYPE html>
<html lang="de">
<head>
<meta charset="utf-8">
<title>Velvet Harbor – Roller Wrap</title>
<link href="https://fonts.googleapis.com/css2?family=Montserrat:wght@400;500;600&display=swap" rel="stylesheet">
<style>
  :root {
    --page: #ffffff;
    --wood-light: #c8ab8a;
    --wood-mid: #b79877;
    --wood-dark: #a8896a;
    --cream: #ece4d7;
    --brown: #8b7560;
    --ink: #3b3330;
    --figure-skin: #e9c9ad;
    --figure-blue: #3d8fc9;
  }
  * { margin: 0; padding: 0; box-sizing: border-box; }
  html, body { width: 831px; height: 1200px; overflow: hidden; background: var(--page); }
  body { font-family: "Montserrat", Arial, sans-serif; color: var(--ink); position: relative; }

  .wrap {
    position: absolute; left: 0; top: 337px;
    width: 831px; height: 526px;
  }
  .wood-band {
    position: absolute; left: 0; width: 100%; height: 60px;
    background: linear-gradient(180deg, var(--wood-light), var(--wood-mid) 55%, var(--wood-dark));
  }
  .wood-band.top { top: 0; }
  .wood-band.bottom { bottom: 0; }
  .panel {
    position: absolute; left: 0; top: 60px; width: 100%; height: 406px;
    background: var(--cream);
  }

  .vertical-title {
    position: absolute; writing-mode: vertical-rl; transform: rotate(180deg);
    font-weight: 600; color: var(--brown); letter-spacing: 2.2px;
    text-transform: uppercase; font-size: 13px; line-height: 17px;
  }
  .vertical-title.left { left: 20px; top: 28px; height: 212px; text-align: center; }
  .vertical-title.right { left: 594px; top: 34px; height: 170px; text-align: center; font-size: 14px; line-height: 19px; }

  .benefits { position: absolute; top: 0; list-style: none; }
  .benefits.de { left: 48px; }
  .benefits.en { left: 637px; }
  .benefits li {
    position: absolute; left: 0;
    padding-left: 15px; font-size: 11px; line-height: 14px;
    text-transform: uppercase; font-weight: 500; color: var(--ink);
    white-space: nowrap;
  }
  .benefits li::before {
    content: ""; position: absolute; left: 0; top: 2px;
    width: 9px; height: 9px; background: var(--brown);
  }

  .brand {
    position: absolute; left: 300px; top: 120px; width: 230px;
    display: flex; align-items: center; justify-content: center; gap: 10px;
  }
  .brand-dot { width: 14px; height: 14px; border-radius: 50%; background: var(--brown); }
  .brand-name {
    font-weight: 600; font-size: 24px; letter-spacing: 3px;
    text-transform: uppercase; color: var(--brown);
  }

  .exercise {
    position: absolute; border-radius: 40px;
    background: linear-gradient(90deg, var(--figure-skin), var(--figure-blue) 55%, var(--figure-skin));
    opacity: .55;
  }
  .exercise.one { left: 18px; top: 273px; width: 260px; height: 102px; }
  .exercise.two { left: 314px; top: 270px; width: 222px; height: 105px; }
  .exercise.three { left: 563px; top: 268px; width: 240px; height: 112px; }

  .origin {
    position: absolute; left: 697px; top: 388px;
    font-size: 7.4px; line-height: 9px; font-weight: 500; text-transform: uppercase;
  }
</style>
</head>
<body>
  <section class="wrap">
    <div class="wood-band top" role="img" aria-label="Wood grain band"></div>

    <div class="panel">
      <h2 class="vertical-title left">Sellbstmassagerolle</h2>

      <ul class="benefits de">
        <li style="top:32px">Für hocheffektives<br>Faszientraining</li>
        <li style="top:71px">Steigert Leistungsvermögen<br>und Elastizität der<br>Muskulatur</li>
        <li style="top:125px">Löst Verspannungen und<br>Verklebungen der Faszien</li>
        <li style="top:165px">Steigert Durchbluting und<br>Regenerationsvermögen</li>
        <li style="top:206px">100% frei von Chemikalien</li>
        <li style="top:233px">Sehr gut hautverträglich</li>
      </ul>

      <div class="brand">
        <span class="brand-dot"></span>
        <span class="brand-name">Velvet Harbor</span>
      </div>

      <h2 class="vertical-title right">Übungen auf<br>der Rückseite</h2>

      <ul class="benefits en">
        <li style="top:32px">For a highly effective<br>workout</li>
        <li style="top:71px">Increase performance<br>and muscle elasticity</li>
        <li style="top:110px">Alleviates strains and<br>posture problems</li>
        <li style="top:150px">Increases blood<br>circulation, rejuvenates<br>muscle</li>
        <li style="top:204px">100% free of chemicals</li>
        <li style="top:231px">Skin-friendly</li>
      </ul>

      <div class="exercise one" role="img" aria-label="Illustration: woman in forearm plank with foam roller under her thighs"></div>
      <div class="exercise two" role="img" aria-label="Illustration: woman lying on her back with foam roller under her upper back, knees bent"></div>
      <div class="exercise three" role="img" aria-label="Illustration: woman rolling her side on the foam roller, supported on one hand"></div>

      <p class="origin">Designes in Germany<br>Made in China</p>
    </div>

    <div class="wood-band bottom" role="img" aria-label="Wood grain band"></div>
  </section>
</body>
</html>
```